Creative, Colorful, Dynamic Infographic for Global Non-Profit

We are a global arts and education non-profit in need of an infographic that illustrates four key skills embedded in our work: Curiosity, Listening, Imagination, Postive Action.
We work primarily with educators, students, and artists who use the power of personal stories to build community and connection and to bridge divides.
Our new brand guidelines, logos, and fonts are here: https://stylekit.example/quillbridge-7
I've attached a mock-up of the graphic and the required text. (Note the attached design was created by a staff person, your final design does not need to be the same. The color scheme and text of the final design should match the brand guidelines above.)
The graphic will be used for both web and print media and should include the purple Quillbridge 7 logo (also attached).
Ideally the final design will delight audiences and spark interest in our work.

```html
<!DOCTYPE html>
<html lang="en">
<head>
<meta charset="utf-8">
<title>Quillbridge 7 – Four Skills</title>
<link rel="stylesheet" href="https://fonts.googleapis.com/css2?family=Figtree:wght@400;700&display=swap">
<style>
  :root {
    --purple: #663399;
    --red: #ee4444;
    --blue: #226bc0;
    --yellow: #e8c946;
    --ink: #1e1d3a;
    --paper: #ffffff;
  }
  html, body {
    margin: 0;
    padding: 0;
    width: 1200px;
    height: 1200px;
    overflow: hidden;
    background: var(--paper);
  }
  .skills-diagram {
    display: block;
    width: 1200px;
    height: 1200px;
    font-family: "Figtree", sans-serif;
  }
  .arm-purple, .quad-purple { fill: var(--purple); }
  .arm-red, .quad-red { fill: var(--red); }
  .arm-blue, .quad-blue { fill: var(--blue); }
  .arm-yellow, .quad-yellow { fill: var(--yellow); }

  .ring-gap { fill: var(--paper); }
  .ring { fill: var(--paper); stroke-width: 30; }
  .ring-purple { stroke: var(--purple); }
  .ring-red { stroke: var(--red); }
  .ring-blue { stroke: var(--blue); }
  .ring-yellow { stroke: var(--yellow); }

  .skill-title { font-weight: 700; font-size: 33px; fill: var(--ink); text-anchor: middle; }
  .skill-text { font-weight: 400; font-size: 32px; fill: var(--ink); text-anchor: middle; }
  .arm-text { font-weight: 400; font-size: 28px; text-anchor: middle; fill: var(--paper); }
  .arm-text-dark { fill: var(--ink); }

  .connector-purple { fill: var(--purple); }
  .connector-red { fill: var(--red); }
  .connector-blue { fill: var(--blue); }
  .connector-yellow { fill: var(--yellow); }
  .connector-arrow { fill: var(--paper); }

  .icon-dark { fill: var(--ink); }
  .icon-light { fill: var(--paper); opacity: 0.9; }
  .icon-ink-soft { fill: var(--ink); opacity: 0.85; }

  .hub { fill: var(--purple); stroke: var(--paper); stroke-width: 8; }
  .hub-name { font-weight: 700; font-size: 28px; fill: var(--paper); text-anchor: middle; }
</style>
</head>
<body>
<svg class="skills-diagram" viewBox="0 0 1920 1920" xmlns="http://www.w3.org/2000/svg" aria-labelledby="diagram-title">
  <title id="diagram-title">Four skills cycle: Curiosity, Listening, Imagination, Positive action</title>

  <g class="star">
    <path class="arm-red" d="M950,140 L985,270 Q1030,400 1146,425 V752 H758 V425 Q870,400 915,270 Z"/>
    <path class="arm-yellow" d="M950,1755 L985,1625 Q1030,1495 1146,1470 V1140 H758 V1470 Q870,1495 915,1625 Z"/>
    <path class="arm-purple" d="M148,944 L265,917 Q400,880 430,752 H758 V1140 H430 Q400,1010 265,973 Z"/>
    <path class="arm-blue" d="M1762,944 L1640,917 Q1510,880 1478,752 H1146 V1140 H1478 Q1510,1010 1640,973 Z"/>
    <rect class="quad-purple" x="758" y="752" width="194" height="194"/>
    <rect class="quad-red" x="952" y="752" width="194" height="194"/>
    <rect class="quad-blue" x="952" y="946" width="194" height="194"/>
    <rect class="quad-yellow" x="758" y="946" width="194" height="194"/>
  </g>

  <g class="arm-labels">
    <rect class="icon-light" x="905" y="305" width="80" height="75" rx="14" role="img" aria-label="Hand holding a tick icon"/>
    <text class="arm-text" x="954">
      <tspan x="954" y="437">Your positive actions</tspan>
      <tspan x="954" y="476">lead to curiosity</tspan>
      <tspan x="954" y="516">about what else</tspan>
      <tspan x="954" y="556">is possible</tspan>
    </text>

    <rect class="icon-light" x="338" y="902" width="56" height="74" rx="12" role="img" aria-label="Curious person icon"/>
    <text class="arm-text">
      <tspan x="488" y="917">Your curiosity</tspan>
      <tspan x="488" y="957">allows you</tspan>
      <tspan x="488" y="996">to listen</tspan>
    </text>

    <rect class="icon-light" x="1424" y="808" width="50" height="66" rx="12" role="img" aria-label="Head with imagination icon"/>
    <text class="arm-text">
      <tspan x="1438" y="917">Your imagination</tspan>
      <tspan x="1438" y="957">can spark</tspan>
      <tspan x="1438" y="996">positive action</tspan>
    </text>

    <rect class="icon-ink-soft" x="924" y="1302" width="56" height="48" rx="10" role="img" aria-label="Listening person icon"/>
    <text class="arm-text arm-text-dark">
      <tspan x="952" y="1385">Your listening</tspan>
      <tspan x="952" y="1424">allows you to</tspan>
      <tspan x="952" y="1464">take in new</tspan>
      <tspan x="952" y="1503">information</tspan>
    </text>
  </g>

  <g class="skill skill-curiosity">
    <circle class="ring-gap" cx="704" cy="698" r="224"/>
    <circle class="ring ring-purple" cx="704" cy="698" r="202"/>
    <rect class="icon-dark" x="670" y="532" width="70" height="92" rx="14" role="img" aria-label="Curious person icon"/>
    <text class="skill-title" x="704" y="660">Curiosity –</text>
    <text class="skill-text">
      <tspan x="704" y="699">Focus on how you can</tspan>
      <tspan x="704" y="738">learn from another's</tspan>
      <tspan x="704" y="778">knowledge and</tspan>
      <tspan x="704" y="817">experience</tspan>
    </text>
  </g>

  <g class="skill skill-positive-action">
    <circle class="ring-gap" cx="1200" cy="698" r="224"/>
    <circle class="ring ring-red" cx="1200" cy="698" r="202"/>
    <rect class="icon-dark" x="1162" y="570" width="84" height="72" rx="14" role="img" aria-label="Hand holding a tick icon"/>
    <text class="skill-title" x="1204" y="677">Positive action -</text>
    <text class="skill-text">
      <tspan x="1204" y="716">Show your words</tspan>
      <tspan x="1204" y="756">and actions</tspan>
      <tspan x="1204" y="795">matter</tspan>
    </text>
  </g>

  <g class="skill skill-listening">
    <circle class="ring-gap" cx="704" cy="1192" r="224"/>
    <circle class="ring ring-yellow" cx="704" cy="1192" r="202"/>
    <rect class="icon-dark" x="656" y="1082" width="76" height="64" rx="14" role="img" aria-label="Listening person icon"/>
    <text class="skill-title" x="702" y="1186">Listening –</text>
    <text class="skill-text">
      <tspan x="702" y="1226">Seek to</tspan>
      <tspan x="702" y="1265">understand</tspan>
      <tspan x="702" y="1305">before speaking</tspan>
    </text>
  </g>

  <g class="skill skill-imagination">
    <circle class="ring-gap" cx="1200" cy="1192" r="224"/>
    <circle class="ring ring-blue" cx="1200" cy="1192" r="202"/>
    <rect class="icon-dark" x="1178" y="1072" width="44" height="64" rx="12" role="img" aria-label="Head with imagination icon"/>
    <text class="skill-title" x="1200" y="1165">Imagination –</text>
    <text class="skill-text">
      <tspan x="1200" y="1204">Consider</tspan>
      <tspan x="1200" y="1244">possibilities beyond</tspan>
      <tspan x="1200" y="1283">what you know</tspan>
    </text>
  </g>

  <g class="connectors">
    <rect class="connector-red" x="946" y="656" width="114" height="84" rx="16"/>
    <path class="connector-arrow" transform="translate(1003,698) rotate(180)" d="M-30,-7 H4 V-24 L30,0 L4,24 V7 H-30 Z"/>

    <rect class="connector-purple" x="663" y="838" width="85" height="114" rx="16"/>
    <path class="connector-arrow" transform="translate(705,895) rotate(90)" d="M-30,-7 H4 V-24 L30,0 L4,24 V7 H-30 Z"/>

    <rect class="connector-yellow" x="843" y="1150" width="115" height="84" rx="16"/>
    <path class="connector-arrow" transform="translate(900,1192)" d="M-30,-7 H4 V-24 L30,0 L4,24 V7 H-30 Z"/>

    <rect class="connector-blue" x="1158" y="938" width="85" height="115" rx="16"/>
    <path class="connector-arrow" transform="translate(1200,995) rotate(-90)" d="M-30,-7 H4 V-24 L30,0 L4,24 V7 H-30 Z"/>
  </g>

  <g class="hub-mark">
    <circle class="hub" cx="950" cy="950" r="110"/>
    <text class="hub-name" x="950" y="960">Quillbridge 7</text>
  </g>
</svg>
</body>
</html>
```